Motion Nest Business Cards

Can all designers please apply the following info on their designs' back-side of the business card: (please see brief file upload ('Info for backside...' - for required info, colours & layout)

SPECIALISING IN INDIVIDUAL PILATES INSTRUCTION
MATWORK – including small apparatus
and STUDIO:
VIVANTE 3 GLIDER
LADDER BARREL
COUNTOUR BARREL
FLEXI DOME
VIM STOOL
KIM-O-LAN

Business Cards for Motion Nest - applying the Motion Nest logo design selected earlier.
Note the business card requires both a front and back side. Please refer to two uploaded ppt-files for type of info required to be displayed, and rough position of where info could be. Require innovative / fresh approach to business card design and use of colour by designers now. Please refer to and use logo as uploaded - also for potential business card colour application.

Dear Designers,

Please note the additional inclusion / upload of two draft ppt-files that try to show where I want what type of information, for both the front & back sides of the required business card, plus an attempt at showing the high-level concept / idea of business info position.

As my 'drafts' obviously lack colour and any ability towards innovative card design or approach – I now rely on your vastly superior graphic design abilities to produce a really great business card for my business…

Looking forward to your submissions!

Kind regards, Merika for: Motion Nest 

Hello all Designers,

Can all designers please apply the following info on their designs' back-side of the business card: (please see / refer to the Brief and specifically the file upload ('Info for backside...' - for required info, colours & layout) - for the backside of the business card).

Info content (without colour, layout etc.):

and STUDIO:

VIVANTE 3 GLIDER

LADDER BARREL

COUNTOUR BARREL

FLEXI DOME

VIM STOOL

KIM-O-LAN

Thank you to all designers that submitted for consideration!

With regards,

Motion Nest

```html
<!DOCTYPE html>
<html lang="en">
<head>
<meta charset="utf-8">
<title>Motion Nest – Business Card</title>
<link rel="stylesheet" href="https://fonts.googleapis.com/css2?family=Didact+Gothic&family=Ubuntu:wght@500;700&display=swap">
<style>
  :root {
    --backdrop: #d6d6d6;
    --card: #ffffff;
    --orange: #e0521f;
    --orange-faint: rgba(224, 82, 31, 0.16);
    --green: #4f6d1e;
    --green-faint: rgba(79, 109, 30, 0.10);
    --ink: #4a4a4a;
  }
  * { box-sizing: border-box; margin: 0; padding: 0; }
  html, body { width: 1200px; height: 871px; overflow: hidden; }
  body {
    background: var(--backdrop);
    position: relative;
    font-family: "Didact Gothic", "Century Gothic", sans-serif;
    color: var(--ink);
  }
  .card {
    position: absolute;
    width: 620px;
    height: 372px;
    background: var(--card);
    box-shadow: 0 6px 18px rgba(0, 0, 0, 0.18);
    overflow: hidden;
  }

  /* ---------- Back side ---------- */
  .card--back { left: 80px; top: 50px; }
  .back__watermark {
    position: absolute;
    left: 0; right: 0; top: 150px;
    text-align: center;
    font-size: 92px;
    color: var(--orange-faint);
    letter-spacing: 1px;
    white-space: nowrap;
  }
  .back__content {
    position: relative;
    text-align: center;
    padding-top: 58px;
  }
  .back__heading {
    font-family: "Ubuntu", sans-serif;
    font-weight: 700;
    font-size: 12.5px;
    color: var(--green);
    letter-spacing: 0.6px;
    line-height: 24px;
  }
  .back__heading--studio { margin-bottom: 8px; }
  .apparatus-list { list-style: none; }
  .apparatus-list li {
    font-size: 13px;
    color: var(--orange);
    letter-spacing: 1px;
    line-height: 29px;
  }

  /* ---------- Front side ---------- */
  .card--front { left: 500px; top: 450px; }
  .front__accent {
    position: absolute;
    right: -90px; top: 40px;
    width: 300px; height: 300px;
    border-radius: 50%;
    background: var(--green-faint);
  }
  .brand {
    position: absolute;
    left: 34px; top: 142px;
  }
  .brand__name {
    display: flex;
    align-items: center;
    gap: 10px;
    font-size: 42px;
    color: var(--orange);
    line-height: 1;
    white-space: nowrap;
  }
  .brand__dot {
    width: 16px; height: 16px;
    border-radius: 50%;
    background: var(--green);
    flex: none;
  }
  .brand__tagline {
    margin-top: 14px;
    font-family: "Ubuntu", sans-serif;
    font-weight: 700;
    font-size: 10.5px;
    color: var(--green);
    letter-spacing: 1.1px;
    white-space: nowrap;
  }
  .details {
    position: absolute;
    left: 312px; top: 92px;
    right: 20px;
  }
  .details__name {
    font-family: "Ubuntu", sans-serif;
    font-weight: 700;
    font-size: 14px;
    color: var(--green);
    letter-spacing: 1.4px;
  }
  .details__title {
    margin-top: 3px;
    font-size: 10.5px;
    color: var(--orange);
    letter-spacing: 0.6px;
  }
  .details__label {
    margin-top: 14px;
    font-family: "Ubuntu", sans-serif;
    font-weight: 700;
    font-size: 11px;
    color: var(--ink);
    letter-spacing: 0.8px;
  }
  .details__address {
    font-style: normal;
    font-size: 12px;
    line-height: 19px;
    letter-spacing: 0.8px;
    margin-top: 2px;
  }
  .contact-list {
    list-style: none;
    margin-top: 16px;
  }
  .contact-list li {
    display: flex;
    align-items: center;
    gap: 12px;
    font-size: 12px;
    letter-spacing: 0.8px;
    line-height: 22px;
  }
  .contact-list svg {
    width: 13px; height: 13px;
    flex: none;
  }
</style>
</head>
<body>

<section class="card card--back" aria-label="Business card, back side">
  <div class="back__watermark" aria-hidden="true">Motion Nest</div>
  <div class="back__content">
    <p class="back__heading">SPECIALISING IN INDIVIDUAL PILATES INSTRUCTION</p>
    <p class="back__heading">MATWORK (INCL. SMALL APPARATUS)</p>
    <p class="back__heading back__heading--studio">STUDIO:</p>
    <ul class="apparatus-list">
      <li>VIVANTE 3 GLIDER</li>
      <li>LADDER BARREL</li>
      <li>COUNTOUR BARREL</li>
      <li>FLEXI DOME</li>
      <li>VIM STOOL</li>
      <li>KIM-O-LAN</li>
    </ul>
  </div>
</section>

<section class="card card--front" aria-label="Business card, front side">
  <div class="front__accent" aria-hidden="true"></div>

  <div class="brand">
    <div class="brand__name"><span class="brand__dot" aria-hidden="true"></span>Motion Nest</div>
    <p class="brand__tagline">BALANCE &nbsp;-&nbsp; STRENGTH &nbsp;-&nbsp; FLEXIBILITY</p>
  </div>

  <div class="details">
    <p class="details__name">MERIKA KALLENBACH</p>
    <p class="details__title">DIPLOMA OF PROFESSIONAL PILATES INSTRUCTION</p>
    <p class="details__label">STUDIO LOCATION:</p>
    <address class="details__address">12 LINDEN CREST AVENUE<br>MARLOW WA 6031</address>
    <ul class="contact-list">
      <li>
        <svg viewBox="0 0 16 16" aria-hidden="true"><path fill="#e0521f" d="M3 1.5h3l1.2 3.2-1.8 1.2a8 8 0 0 0 4.7 4.7l1.2-1.8 3.2 1.2v3a1.5 1.5 0 0 1-1.6 1.5A13 13 0 0 1 1.5 3.1 1.5 1.5 0 0 1 3 1.5z"/></svg>
        040 555 0192
      </li>
      <li>
        <svg viewBox="0 0 16 16" aria-hidden="true"><rect x="1" y="3" width="14" height="10" rx="1" fill="none" stroke="#e0521f" stroke-width="1.6"/><path d="M1.5 3.8 8 9l6.5-5.2" fill="none" stroke="#e0521f" stroke-width="1.6"/></svg>
        INFO@MOTIONNEST.COM
      </li>
      <li>
        <svg viewBox="0 0 16 16" aria-hidden="true"><circle cx="8" cy="8" r="6.5" fill="none" stroke="#e0521f" stroke-width="1.5"/><ellipse cx="8" cy="8" rx="2.8" ry="6.5" fill="none" stroke="#e0521f" stroke-width="1.2"/><path d="M1.5 8h13" stroke="#e0521f" stroke-width="1.2"/></svg>
        WWW.MOTIONNEST.COM.AU
      </li>
    </ul>
  </div>
</section>

</body>
</html>
```